Lawn mowing business card design

We need a business card design for our lawn mowing and gardening business which is located in the Northern Beaches of Sydney. Our business name is Meadowline Turf and our logo is predominantly green and yellow in color. Please see our website at www.meadowlineturf.com.au for design ideas. The business targets young professionals and older clientele. As such the font should be easy to read, but I also want the business card to be colorful and stand out.

Target Market(s)

young professionals

Industry/Entity Type

Lawn Care

Contact Information for Business Card

Meadowline Turf, Gareth Pellow, 0478559201, www.meadowlineturf.com.au, email: meadowlineturf@mailbox-example.com

Font styles to use
Serif

Colors
9bcb3b
fbed22

Requirements
Must have
• Must include the details listed above. Must include the attached logo.
Nice to have
• Logo attached with two copies. The logo without any writing is high quality, please feel free to be creative with the text stating our business name "Meadowline Turf" using this file.

```html
<!DOCTYPE html>
<html lang="en">
<head>
<meta charset="utf-8">
<title>Meadowline Turf – Business Card</title>
<link href="https://fonts.googleapis.com/css2?family=Open+Sans:wght@300;400;700;800&display=swap" rel="stylesheet">
<style>
  :root {
    --bg: #e9e6df;
    --grass-light: #9bcb3b;
    --grass-mid: #7cbf2e;
    --grass-dark: #4f9a1f;
    --leaf-green: #2f8a3e;
    --soil-brown: #3e2c23;
    --sun-yellow: #fbed22;
    --ribbon: #f2f2f0;
    --ink-dark: #2b2b2b;
    --ink-grey: #6a6a6a;
    --paper: #ffffff;
    --on-soil: #f3efe9;
  }
  * { box-sizing: border-box; margin: 0; padding: 0; }
  html, body { width: 1200px; height: 950px; overflow: hidden; }
  body {
    background: var(--bg);
    font-family: "Open Sans", Arial, sans-serif;
    position: relative;
  }
  .card {
    position: absolute;
    width: 560px;
    height: 320px;
    overflow: hidden;
    box-shadow: 0 6px 18px rgba(0,0,0,.18);
  }

  /* ---------- Front ---------- */
  .card-front { left: 60px; top: 130px; }
  .front-lawn {
    position: absolute; left: 0; top: 0; width: 330px; height: 100%;
    background: linear-gradient(180deg, var(--grass-dark) 0%, var(--grass-mid) 18%, var(--grass-light) 50%, var(--grass-mid) 82%, var(--grass-dark) 100%);
  }
  .front-soil {
    position: absolute; right: 0; top: 0; width: 230px; height: 100%;
    background: var(--soil-brown);
  }
  .contact-list {
    position: absolute; right: 0; top: 130px; width: 230px;
    list-style: none; color: var(--on-soil);
    font-size: 11px; font-weight: 300; line-height: 2.1;
    padding: 0 10px 0 14px;
    white-space: nowrap;
  }
  .card-front .mascot-area {
    position: absolute; left: 90px; top: 58px; width: 170px; height: 140px;
  }
  .mascot-area {
    border-radius: 14px;
    background: radial-gradient(circle at 50% 45%, var(--sun-yellow) 0%, #e7c823 45%, var(--leaf-green) 100%);
  }
  .name-ribbon {
    position: absolute; left: 135px; top: 176px; width: 180px; height: 38px;
    background: var(--ribbon);
    display: flex; align-items: center; justify-content: center;
    box-shadow: 0 2px 4px rgba(0,0,0,.2);
  }
  .name-ribbon .person-name {
    font-size: 18px; font-weight: 800; color: var(--ink-dark); letter-spacing: .2px;
    white-space: nowrap;
  }

  /* ---------- Back ---------- */
  .card-back { left: 580px; top: 500px; background: var(--paper); }
  .services {
    position: absolute; left: 40px; top: 34px;
    list-style: none; color: var(--ink-grey);
    font-size: 13px; font-weight: 400; line-height: 1.55;
  }
  .services li::before {
    content: ""; display: inline-block; width: 5px; height: 5px; border-radius: 50%;
    background: var(--leaf-green); margin-right: 9px; vertical-align: middle;
  }
  .brand-block {
    position: absolute; right: 36px; bottom: 40px; width: 220px;
    display: flex; flex-direction: column; align-items: center; gap: 12px;
  }
  .brand-block .mascot-area { width: 150px; height: 120px; }
  .brand-name {
    display: flex; align-items: center; gap: 8px;
    font-size: 20px; font-weight: 800; color: var(--ink-dark);
    white-space: nowrap;
  }
  .brand-dot { width: 12px; height: 12px; border-radius: 50%; background: var(--leaf-green); }
</style>
</head>
<body>

  <section class="card card-front" aria-label="Business card front">
    <div class="front-lawn" role="img" aria-label="Lush green grass lawn backdrop"></div>
    <div class="front-soil"></div>
    <div class="mascot-area" role="img" aria-label="Yellow cartoon lawn mower mascot on a green triangle"></div>
    <div class="name-ribbon"><span class="person-name">Gareth Pellow</span></div>
    <ul class="contact-list">
      <li>0478559201</li>
      <li>meadowlineturf@mailbox-example.com</li>
      <li>www.meadowlineturf.com.au</li>
    </ul>
  </section>

  <section class="card card-back" aria-label="Business card back">
    <ul class="services">
      <li>lawn mowing</li>
      <li>Edging</li>
      <li>Blowing</li>
      <li>Hedging</li>
      <li>Pruning</li>
      <li>Tree lopping</li>
      <li>Weeding</li>
      <li>Planting</li>
      <li>Rubbish removal</li>
      <li>Garden care &amp; advice</li>
    </ul>
    <div class="brand-block">
      <div class="mascot-area" role="img" aria-label="Yellow cartoon lawn mower mascot on a green triangle"></div>
      <div class="brand-name"><span class="brand-dot"></span>Meadowline Turf</div>
    </div>
  </section>

</body>
</html>
```